Tidewell Cargo Links Website

We require a prominent webpage for a new concept on an old idea. We are a freight forwarding company in the Bahamas that will streamline the import process in the Bahamas for clients while offering both airfreight and seafreight import and export services . We would like the final design to communicate a professional image with stable service offering. Please view www.korvanfreight.example to see an example of what we require. Also view the site www.pemla.tariffgate.example and dorvelin.example. We will requier integration with these and other websites.

Target Market(s)

Small (<100) and medium (100-500) commercial businesses that require full importation services.

Industry/Entity Type

Freight Forwarding

Coding

Coded - Design and coding required

Number of Pages Required

5+ page

Colors

Designer to choose colors to be used in the design.

Requirements
Must have
• Core Website Development – Front End
• 1. Website Design
• 2. Coding and Development
• 4. Graphics
• 5. Social Media Integrations
• 6. Email Integration
• 7. Security / SSL Integrations
• 8. User Dashboard / Account
• 9. Customer Signup Integration
• 10. eCommerceOnlinePayment
• 11. XML–APIDevelopmentforDorvelin
• 12. DorvelinIntegrations

```html
<!DOCTYPE html>
<html lang="en">
<head>
<meta charset="utf-8">
<title>Tidewell Cargo Links</title>
<link href="https://fonts.googleapis.com/css2?family=Roboto:wght@400;500;700;900&family=Open+Sans:ital,wght@0,400;0,600;0,700;1,400;1,600&display=swap" rel="stylesheet">
<style>
:root{
  --navy:#1c2a4e;
  --navy-deep:#152241;
  --red:#d12e2e;
  --red-band:#c93a36;
  --ink:#1a1a1a;
  --grey:#666;
  --line:#d9d9d9;
  --white:#fff;
  --star:#f2d53c;
}
*{box-sizing:border-box;margin:0;padding:0}
html,body{width:1200px;height:2826px;overflow:hidden;background:var(--white)}
body{position:relative;font-family:"Open Sans",sans-serif;color:var(--ink)}
.abs{position:absolute}
.heading{font-family:"Roboto",sans-serif;font-weight:500;text-transform:uppercase;color:var(--ink)}

/* header */
.topbar{top:16px;right:94px;font:600 15px "Open Sans",sans-serif;display:flex;gap:14px;align-items:center}
.topbar svg{width:13px;height:13px;fill:var(--red);margin-right:6px;vertical-align:-1px}
.nav{top:58px;right:94px;display:flex;gap:44px;font:500 15px "Roboto",sans-serif;text-transform:uppercase;align-items:center}
.nav .active{color:var(--red)}
.brand{left:84px;top:-12px;width:216px;height:216px;border-radius:50%;background:var(--white);display:flex;align-items:center;justify-content:center;text-align:center;z-index:3}
.brand span{font:700 24px/1.2 "Roboto",sans-serif;color:var(--navy);width:150px}

/* hero */
.hero{top:90px;left:0;width:1200px;height:540px;background:linear-gradient(180deg,#8a7a5a 0%,#5e5a55 40%,#3a4652 100%)}
.hero-title{top:258px;left:0;width:1200px;text-align:center;font:700 64px/76px "Roboto",sans-serif;color:var(--white);text-transform:uppercase}
.dots{top:502px;left:567px;display:flex;gap:4px}
.dots i{width:14px;height:14px;border-radius:50%;border:2px solid var(--white);display:block}
.dots i:first-child{background:var(--white)}
.hero-curve{top:440px;left:0}

/* welcome */
.welcome-title{top:694px;width:1200px;text-align:center;font-size:31px}
.welcome-text{top:748px;left:240px;width:720px;text-align:center;font-size:15px;line-height:27px;color:var(--grey)}
.service{width:240px;text-align:center;top:843px}
.service .ring{width:148px;height:148px;margin:0 auto;border-radius:50%;border:4px solid var(--navy);display:flex;align-items:center;justify-content:center}
.service .ring .inner{width:128px;height:128px;border-radius:50%;border:1px solid var(--navy);display:flex;align-items:center;justify-content:center}
.service h3{margin-top:36px;font:500 21px/26px "Roboto",sans-serif;height:52px}
.service p{margin-top:18px;font-size:14px;line-height:25px;color:var(--grey)}
.service a{display:block;margin-top:14px;font:700 15px "Open Sans",sans-serif;color:var(--red);text-transform:uppercase}

/* what we do */
.wwd{top:1243px;left:0;width:1200px;height:453px;background:linear-gradient(180deg,var(--navy) 0%,var(--navy-deep) 100%)}
.wwd-frame{top:1285px;left:100px;width:612px;height:369px;border:2px solid var(--white)}
.wwd-title{top:1342px;left:142px;font:500 27px "Roboto",sans-serif;color:var(--white)}
.wwd-text{top:1392px;left:142px;width:490px;font-size:14.5px;line-height:26px;color:var(--white)}
.btn{display:flex;align-items:center;justify-content:center;background:var(--red);color:var(--white);font:600 15px "Open Sans",sans-serif;text-transform:uppercase;border-radius:22px}
.wwd-btn{top:1547px;left:143px;width:134px;height:42px}
.video{top:1317px;left:627px;width:471px;height:303px;border:4px solid var(--white);background:linear-gradient(135deg,#7a6a4e,#b89a6a 50%,#5b5048)}
.play{left:207px;top:123px;width:58px;height:58px;border-radius:50%;background:#111;display:flex;align-items:center;justify-content:center}

/* why */
.why-title{top:1762px;width:1200px;text-align:center;font-size:31px}
.why{top:1835px;width:180px;text-align:center}
.why .circ{width:110px;height:110px;margin:0 auto;border-radius:50%;border:1px solid #444;display:flex;align-items:center;justify-content:center}
.why.on .circ{border-color:var(--red)}
.why p{margin-top:20px;font-size:15px;line-height:22px;color:#333}
.why.on p{color:var(--red)}
.why svg{width:40px;height:40px;fill:var(--navy)}
.why.on svg{fill:var(--red)}

/* testimonials */
.testi-band{top:2076px;left:0;width:1200px;height:500px;background:var(--red-band)}
.testi-title{top:2132px;width:1200px;text-align:center;font:500 30px "Roboto",sans-serif;color:var(--white);text-transform:uppercase}
.testi{top:2200px;width:340px;color:var(--white)}
.avatar{left:0;top:0;width:72px;height:72px;border-radius:50%;border:3px solid var(--white);background:linear-gradient(160deg,#e9d3c2,#9b8a80)}
.quote{position:absolute;left:88px;top:6px;width:252px;font:italic 400 12.5px/22px "Open Sans",sans-serif}
.quote b{font:italic 700 20px "Roboto",sans-serif;margin-right:6px}
.who{position:absolute;left:88px;top:94px;font:600 11px "Open Sans",sans-serif;text-transform:uppercase}
.role{position:absolute;left:88px;top:114px;font:italic 600 10.5px "Open Sans",sans-serif}
.stars{position:absolute;left:88px;top:148px;display:flex;gap:4px}
.stars svg{width:18px;height:18px}
.arrow{top:2256px;width:36px;height:36px;border-radius:50%;border:1.5px solid var(--white);display:flex;align-items:center;justify-content:center}
.arrow svg{width:12px;height:12px;stroke:var(--white);fill:none;stroke-width:2}

/* footer */
.foot-curve{top:2420px;left:0}
.foot-brand{left:96px;top:2530px;width:196px;height:170px;display:flex;align-items:center;justify-content:center;text-align:center}
.foot-brand span{font:700 26px/1.2 "Roboto",sans-serif;color:var(--navy)}
.foot-head{top:2532px;font:500 17px "Roboto",sans-serif;text-transform:uppercase}
.links{top:2574px;left:367px;font-size:12.5px;line-height:25px;color:#333;list-style:none}
.nl-text{top:2574px;left:546px;width:260px;font-size:12.5px;line-height:22px;color:#333}
.nl-input{top:2632px;left:546px;width:254px;height:34px;border-bottom:1px solid var(--line);font-size:12px;color:#999;padding:10px 0 0 10px}
.nl-btn{top:2682px;left:546px;width:104px;height:32px;border:1.5px solid var(--red);border-radius:16px;color:var(--red);font:600 12px "Open Sans",sans-serif;text-transform:uppercase;display:flex;align-items:center;justify-content:center}
.contact{left:870px;font-size:12.5px;line-height:22px;color:#333;display:flex;gap:16px}
.contact svg{width:14px;height:14px;fill:var(--navy);flex:none;margin-top:4px}
.rule{top:2748px;left:100px;width:1000px;height:1px;background:var(--line)}
.copy{top:2775px;left:100px;font-size:12px;color:#333}
.social{top:2770px;left:973px;display:flex;gap:8px}
.social i{display:block;width:28px;height:28px;border-radius:50%;border:1px solid #555}
</style>
</head>
<body>

<!-- header -->
<div class="abs topbar">
  <span><svg viewBox="0 0 24 24"><path d="M6.6 10.8a15.1 15.1 0 006.6 6.6l2.2-2.2c.3-.3.7-.4 1-.2 1.1.4 2.3.6 3.6.6.6 0 1 .4 1 1V20c0 .6-.4 1-1 1A17 17 0 013 4c0-.6.4-1 1-1h3.5c.6 0 1 .4 1 1 0 1.3.2 2.5.6 3.6.1.3 0 .7-.2 1z"/></svg>(242)555-0183 (84)</span>
  <span style="color:#999">|</span>
  <span><svg viewBox="0 0 24 24"><path d="M2 5h20v14H2z M2 5l10 8 10-8" /></svg>sales@tidewellcargo.example</span>
</div>
<nav class="abs nav">
  <span class="active">Home</span><span>About</span><span>Industries</span><span>Services</span><span>Blog</span><span>Contact</span>
  <svg width="15" height="15" viewBox="0 0 24 24" fill="none" stroke="#1a1a1a" stroke-width="3"><circle cx="10" cy="10" r="7"/><path d="M15 15l7 7"/></svg>
</nav>

<!-- hero -->
<div class="abs hero" role="img" aria-label="Aerial photo of a container port with stacked shipping containers and cranes"></div>
<svg class="abs hero-curve" width="1200" height="200" viewBox="0 0 1200 200">
  <path d="M0 70 Q600 250 1200 70 L1200 200 L0 200 Z" fill="#fff"/>
  <path d="M0 70 Q600 250 1200 70" fill="none" stroke="#1c2a4e" stroke-width="3"/>
  <path d="M0 84 Q600 260 1200 84 Q600 300 0 92 Z" fill="#d12e2e"/>
</svg>
<div class="abs brand"><span>Tidewell Cargo Links</span></div>
<h1 class="abs hero-title">Your Forwarding<br>Solutions Provider!!</h1>
<div class="abs dots"><i></i><i></i><i></i><i></i></div>

<!-- welcome -->
<h2 class="abs heading welcome-title">Welcome to Tidewell Cargo Links</h2>
<p class="abs welcome-text">Our mission is to constantly exceed customer expectations by providing superior freight forwarding and global transportation solutions including customs clearance and logistics services.</p>

<div class="abs service" style="left:87px">
  <div class="ring"><div class="inner"><svg width="70" height="50" viewBox="0 0 70 50" fill="#d12e2e"><rect x="14" y="8" width="10" height="10"/><rect x="26" y="8" width="10" height="10"/><rect x="20" y="20" width="30" height="10"/><path d="M4 32h62l-8 12H12z"/></svg></div></div>
  <h3>Freight Forwarding<br>&amp; Logistics</h3>
  <p>We offer Freight Forwarding &amp; Logistics Services that</p>
  <a>Read More</a>
</div>
<div class="abs service" style="left:349px">
  <div class="ring"><div class="inner"><svg width="50" height="64" viewBox="0 0 50 64" fill="#d12e2e"><path d="M25 2a22 22 0 00-22 22c0 16 22 38 22 38s22-22 22-38A22 22 0 0025 2z"/><circle cx="25" cy="24" r="9" fill="#fff"/></svg></div></div>
  <h3>Freight<br>Consolidation</h3>
  <p>The Freight Consolidation Services for shipments are the cost</p>
  <a>Read More</a>
</div>
<div class="abs service" style="left:609px">
  <div class="ring"><div class="inner"><svg width="64" height="64" viewBox="0 0 64 64" fill="none" stroke="#d12e2e" stroke-width="3"><rect x="26" y="16" width="30" height="40"/><path d="M32 28h18M32 36h18M32 44h12"/><circle cx="44" cy="12" r="8"/><circle cx="16" cy="18" r="6"/><path d="M6 56V34a10 10 0 0120 0"/></svg></div></div>
  <h3>Customs<br>Clearance</h3>
  <p>The Import and Export Customs Clearance Services offered</p>
  <a>Read More</a>
</div>
<div class="abs service" style="left:871px">
  <div class="ring"><div class="inner"><svg width="70" height="56" viewBox="0 0 70 56" fill="#d12e2e"><path d="M2 20L35 2l33 18v4H2z"/><rect x="8" y="26" width="54" height="28"/><g fill="#fff"><rect x="18" y="32" width="34" height="4"/><rect x="18" y="40" width="34" height="4"/><rect x="18" y="48" width="34" height="4"/></g></svg></div></div>
  <h3>Warehousing<br>Services</h3>
  <p>We offer dedicated warehousing services to our clients</p>
  <a>Read More</a>
</div>

<!-- what we do -->
<div class="abs wwd"></div>
<div class="abs wwd-frame"></div>
<h2 class="abs wwd-title">WHAT WE DO</h2>
<p class="abs wwd-text">Nam libero tempore, cum soluta nobis est eligendi optio cumquenihil impedit quo minus id quod maxime placeat facere possimus, omnis voluptas assumenda est, omnis dolor repellendus. Temporib autem quibusdam et aut officiis debitis aut rerum necessitatibus saepe eve niet ut et voluptates repudiandae sint et.</p>
<div class="abs btn wwd-btn">Read More</div>
<div class="abs video" role="img" aria-label="Video still of two warehouse workers checking stock between pallet racks">
  <div class="abs play"><svg width="22" height="22" viewBox="0 0 24 24" fill="#fff"><path d="M6 3l15 9-15 9z"/></svg></div>
</div>

<!-- why choose us -->
<h2 class="abs heading why-title">Why Choose Us?</h2>
<div class="abs why on" style="left:64px"><div class="circ"><svg viewBox="0 0 24 24"><path d="M21 16v-2l-8-5V3.5a1.5 1.5 0 00-3 0V9l-8 5v2l8-2.5V19l-2 1.5V22l3.5-1 3.5 1v-1.5L13 19v-5.5z" transform="rotate(45 12 12)"/></svg></div><p>Superior Freight<br>Forwarding</p></div>
<div class="abs why" style="left:242px"><div class="circ"><svg viewBox="0 0 24 24"><circle cx="12" cy="12" r="10"/><path d="M7 7c2 1 3 0 4 2s-1 3 1 4 2 3 1 5M15 4c0 2 2 2 3 3" stroke="#fff" stroke-width="1.6" fill="none"/></svg></div><p>Global<br>Transportation</p></div>
<div class="abs why" style="left:421px"><div class="circ"><svg viewBox="0 0 24 24"><path d="M4 3h16v9c0 5-4 8-8 10-4-2-8-5-8-10z"/><path d="M12 5v15c3-1.5 6-4 6-8V5z" fill="#fff"/></svg></div><p>Safe<br>Delivery</p></div>
<div class="abs why" style="left:598px"><div class="circ"><svg viewBox="0 0 24 24"><path d="M2 3h9l11 11-8 8L3 11z"/><circle cx="7" cy="7" r="2" fill="#fff"/></svg></div><p>Cost<br>Effective</p></div>
<div class="abs why" style="left:777px"><div class="circ"><svg viewBox="0 0 24 24"><path d="M12 2l11 20H1z"/><rect x="11" y="9" width="2" height="7" fill="#fff"/><rect x="11" y="17.5" width="2" height="2" fill="#fff"/></svg></div><p>Hassle-free<br>Clearance</p></div>
<div class="abs why" style="left:956px"><div class="circ"><svg viewBox="0 0 24 24"><path d="M22 2L2 10l7 3 2 8 3-5 5 3z"/></svg></div><p>Quick and<br>Effective</p></div>

<!-- testimonials -->
<div class="abs testi-band" role="img" aria-label="Red-tinted photo of a cargo ship loaded with containers"></div>
<h2 class="abs testi-title">Client Testimonials</h2>

<div class="abs testi" style="left:96px">
  <div class="abs avatar" role="img" aria-label="Client portrait"></div>
  <p class="quote"><b>“</b>At vero eos et accusamus et iustodio dignissimos ducimus qui blanditiipraesnt ium voluptatum deleniti atq.</p>
  <div class="who">Marisol Vetter</div>
  <div class="role">Financial Services Professional</div>
  <div class="stars"><svg viewBox="0 0 24 24" fill="#f2d53c"><path d="M12 2l3 7 7 .6-5.4 4.7L18 22l-6-3.7L6 22l1.4-7.7L2 9.6 9 9z"/></svg><svg viewBox="0 0 24 24" fill="#f2d53c"><path d="M12 2l3 7 7 .6-5.4 4.7L18 22l-6-3.7L6 22l1.4-7.7L2 9.6 9 9z"/></svg><svg viewBox="0 0 24 24" fill="#f2d53c"><path d="M12 2l3 7 7 .6-5.4 4.7L18 22l-6-3.7L6 22l1.4-7.7L2 9.6 9 9z"/></svg><svg viewBox="0 0 24 24" fill="#f2d53c"><path d="M12 2l3 7 7 .6-5.4 4.7L18 22l-6-3.7L6 22l1.4-7.7L2 9.6 9 9z"/></svg><svg viewBox="0 0 24 24" fill="none" stroke="#f2d53c" stroke-width="2"><path d="M12 2l3 7 7 .6-5.4 4.7L18 22l-6-3.7L6 22l1.4-7.7L2 9.6 9 9z"/></svg></div>
</div>
<div class="abs testi" style="left:446px">
  <div class="abs avatar" role="img" aria-label="Client portrait"></div>
  <p class="quote"><b>“</b>At vero eos et accusamus et iustodio dignissimos ducimus qui blanditiipraesnt ium voluptatum deleniti atq.</p>
  <div class="who">Dorian K. Ashby</div>
  <div class="role">National Urban Fellow at the Houston</div>
  <div class="stars"><svg viewBox="0 0 24 24" fill="#f2d53c"><path d="M12 2l3 7 7 .6-5.4 4.7L18 22l-6-3.7L6 22l1.4-7.7L2 9.6 9 9z"/></svg><svg viewBox="0 0 24 24" fill="#f2d53c"><path d="M12 2l3 7 7 .6-5.4 4.7L18 22l-6-3.7L6 22l1.4-7.7L2 9.6 9 9z"/></svg><svg viewBox="0 0 24 24" fill="#f2d53c"><path d="M12 2l3 7 7 .6-5.4 4.7L18 22l-6-3.7L6 22l1.4-7.7L2 9.6 9 9z"/></svg><svg viewBox="0 0 24 24" fill="#f2d53c"><path d="M12 2l3 7 7 .6-5.4 4.7L18 22l-6-3.7L6 22l1.4-7.7L2 9.6 9 9z"/></svg><svg viewBox="0 0 24 24" stroke="#f2d53c" stroke-width="2" fill="none"><path d="M12 2l3 7 7 .6-5.4 4.7L18 22l-6-3.7L6 22l1.4-7.7L2 9.6 9 9z"/><path d="M12 2v16.3L6 22l1.4-7.7L2 9.6 9 9z" fill="#f2d53c"/></svg></div>
</div>
<div class="abs testi" style="left:795px">
  <div class="abs avatar" role="img" aria-label="Client portrait"></div>
  <p class="quote"><b>“</b>At vero eos et accusamus et iustodio dignissimos ducimus qui blanditiipraesnt ium voluptatum deleniti atq.</p>
  <div class="who">Lena Brockway</div>
  <div class="role">Creative Strategist | Entrepreneur &amp; Upcoming</div>
  <div class="stars"><svg viewBox="0 0 24 24" fill="#f2d53c"><path d="M12 2l3 7 7 .6-5.4 4.7L18 22l-6-3.7L6 22l1.4-7.7L2 9.6 9 9z"/></svg><svg viewBox="0 0 24 24" fill="#f2d53c"><path d="M12 2l3 7 7 .6-5.4 4.7L18 22l-6-3.7L6 22l1.4-7.7L2 9.6 9 9z"/></svg><svg viewBox="0 0 24 24" fill="#f2d53c"><path d="M12 2l3 7 7 .6-5.4 4.7L18 22l-6-3.7L6 22l1.4-7.7L2 9.6 9 9z"/></svg><svg viewBox="0 0 24 24" fill="#f2d53c"><path d="M12 2l3 7 7 .6-5.4 4.7L18 22l-6-3.7L6 22l1.4-7.7L2 9.6 9 9z"/></svg><svg viewBox="0 0 24 24" fill="none" stroke="#f2d53c" stroke-width="2"><path d="M12 2l3 7 7 .6-5.4 4.7L18 22l-6-3.7L6 22l1.4-7.7L2 9.6 9 9z"/></svg></div>
</div>
<div class="abs arrow" style="left:29px"><svg viewBox="0 0 12 12"><path d="M8 1L3 6l5 5"/></svg></div>
<div class="abs arrow" style="left:1133px"><svg viewBox="0 0 12 12"><path d="M4 1l5 5-5 5"/></svg></div>

<!-- footer -->
<svg class="abs foot-curve" width="1200" height="160" viewBox="0 0 1200 160">
  <path d="M0 142 Q600 -40 1200 142 L1200 160 L0 160 Z" fill="#fff"/>
  <path d="M0 142 Q600 -40 1200 142" fill="none" stroke="#1c2a4e" stroke-width="6"/>
</svg>
<div class="abs foot-brand"><span>Tidewell Cargo Links</span></div>

<h3 class="abs foot-head" style="left:367px">Quick Links</h3>
<ul class="abs links"><li>Help</li><li>FAQ</li><li>Support</li><li>Sitemap</li><li>Terms Of Use</li><li>Privacy Statement</li></ul>

<h3 class="abs foot-head" style="left:546px">Newsletter Subscription</h3>
<p class="abs nl-text">Register your Email Address to get Information about us</p>
<div class="abs nl-input">Email Address</div>
<div class="abs nl-btn">Subscribe</div>

<h3 class="abs foot-head" style="left:870px">Contact Us</h3>
<div class="abs contact" style="top:2578px"><svg viewBox="0 0 24 24"><path d="M12 2a7 7 0 00-7 7c0 5 7 13 7 13s7-8 7-13a7 7 0 00-7-7zm0 9.5A2.5 2.5 0 1112 6.5a2.5 2.5 0 010 5z"/></svg><span>P.O. Box QK-40217<br>Harbour Town, Bahamas</span></div>
<div class="abs contact" style="top:2644px"><svg viewBox="0 0 24 24"><path d="M6.6 10.8a15.1 15.1 0 006.6 6.6l2.2-2.2c.3-.3.7-.4 1-.2 1.1.4 2.3.6 3.6.6.6 0 1 .4 1 1V20c0 .6-.4 1-1 1A17 17 0 013 4c0-.6.4-1 1-1h3.5c.6 0 1 .4 1 1 0 1.3.2 2.5.6 3.6.1.3 0 .7-.2 1z"/></svg><span>(242)555-0183 &nbsp;|&nbsp; (242)555-0184</span></div>
<div class="abs contact" style="top:2686px"><svg viewBox="0 0 24 24"><path d="M2 5h20v14H2z" /><path d="M2 5l10 8 10-8" fill="none" stroke="#fff" stroke-width="2"/></svg><span>sales@tidewellcargo.example</span></div>

<div class="abs rule"></div>
<p class="abs copy">Copyrights © 2018, Tidewell Cargo Links. &nbsp;All rights reserved.</p>
<div class="abs social"><i></i><i></i><i></i><i></i></div>

</body>
</html>
```